Bramwell Quayle Lending Solutions business card design

Need a business card design for my mortgage broking business Bramwell Quayle Lending Solutions.

Target Market(s)

Mortgage clients/colleagues

Industry/Entity Type

Business

Requirements
Must have
• Must utilise logo attached. Possibly have logo only on back of card. my name & contact details on front and something creative?

Must incorporate purple/black/white in colour scheme.

Must incorporate tag line 'the mortgage detectives' under logo - using a script style fint. UPDATE: Mistral doesn't seem to be working on the card. Happy for you to try a different font. preferably a script style font.

Standard business card size.
Nice to have
• Try and incorporate the detective theme - but keep it looking sharp and professional.
Have attached some sample designs - does not have to be this - happy to review any ideas you may have.

```html
<!DOCTYPE html>
<html lang="en">
<head>
<meta charset="utf-8">
<title>Bramwell Quayle Lending Solutions – Business Card</title>
<link href="https://fonts.googleapis.com/css2?family=Caveat:wght@700&display=swap" rel="stylesheet">
<style>
  :root {
    --paper: #ffffff;
    --panel: #0b0b0b;
    --ink-light: #ffffff;
    --ink-navy: #1c0e8e;
  }
  * { margin: 0; padding: 0; box-sizing: border-box; }
  html, body {
    width: 1200px; height: 900px; overflow: hidden;
    background: var(--paper);
  }
  .card { display: block; width: 1200px; height: 900px; }
  .card text { font-family: "Caveat", cursive; font-weight: 700; }
  .details-panel { fill: var(--panel); }
  .detail-line { fill: var(--ink-light); font-size: 120px; }
  .website { fill: var(--ink-navy); font-size: 120px; }
  .brand-name { fill: var(--ink-navy); font-size: 50px; }
  .brand-dot { fill: var(--ink-navy); }
  .brand-tagline { fill: var(--ink-navy); font-size: 40px; }
</style>
</head>
<body>
  <svg class="card" viewBox="0 0 1200 900" xmlns="http://www.w3.org/2000/svg">
    <defs>
      <filter id="soft-shadow" x="-5%" y="-20%" width="110%" height="140%">
        <feDropShadow dx="2" dy="3" stdDeviation="2" flood-color="#000" flood-opacity="0.35"/>
      </filter>
    </defs>
    <rect class="details-panel" x="8" y="14" width="1184" height="676"/>
    <text class="detail-line name" x="18" y="128" textLength="545" lengthAdjust="spacingAndGlyphs">Managing Director Harriet Lowndes</text>
    <text class="detail-line tagline" x="18" y="298" textLength="620" lengthAdjust="spacingAndGlyphs">Non-Conforming Mortgage Specialists</text>
    <text class="detail-line address" x="18" y="478" textLength="1162" lengthAdjust="spacingAndGlyphs">Carrow House, Level 1, 214 Little Ferris Street Melbourne 3000</text>
    <text class="detail-line contact" x="18" y="652" textLength="890" lengthAdjust="spacingAndGlyphs">Ph: 0491 570 118 e: harriet@bqlending.com.au</text>

    <text class="website" x="20" y="822" textLength="475" lengthAdjust="spacingAndGlyphs" filter="url(#soft-shadow)">w: www.bqlending.com.au</text>

    <g class="brand-mark">
      <circle class="brand-dot" cx="822" cy="774" r="20"/>
      <text class="brand-name" x="855" y="792" textLength="325" lengthAdjust="spacingAndGlyphs">Bramwell Quayle</text>
      <text class="brand-tagline" x="1180" y="848" text-anchor="end" textLength="325" lengthAdjust="spacingAndGlyphs">the mortgage detectives</text>
    </g>
  </svg>
</body>
</html>
```